Aesthetics Company Flyer (description of services)

We need a 5.5"x8.5" flyer describing the services we offer at velvet horizon aesthetics. We are an aesthetics company located in Conroe TX. Our products and services can be found at www.vhaesthetics-demo.com/services . We would like to see designs that are cohesive with our brand and website: https://www.vhaesthetics-demo.com/

```html
<!DOCTYPE html>
<html lang="en">
<head>
<meta charset="utf-8">
<title>Velvet Horizon Aesthetics — Our Services</title>
<link rel="stylesheet" href="https://fonts.googleapis.com/css2?family=Cormorant+Garamond:wght@500;600;700&family=Cormorant+SC:wght@600;700&display=swap">
<style>
  :root{
    --bg:#e4e4e4;
    --paper:#f6f6f7;
    --lavender:#b19cd6;
    --lavender-deep:#9a82c6;
    --ink:#2b2b2b;
    --muted:#555;
    --white:#ffffff;
    --photo-warm:linear-gradient(135deg,#d9a07a,#8a6a58);
    --photo-cool:linear-gradient(135deg,#e8e4e2,#b9aea8);
    --photo-skin:linear-gradient(135deg,#d8b9a6,#9c7d6c);
    --photo-peel:linear-gradient(135deg,#d9c25a,#4a4a4a);
  }
  *{box-sizing:border-box;margin:0;padding:0}
  html,body{width:1200px;height:900px;overflow:hidden}
  body{background:var(--bg);font-family:"Cormorant Garamond",Georgia,serif;color:var(--ink)}
  .flyer{position:absolute;left:335px;top:40px;width:530px;height:820px;background:var(--paper);box-shadow:0 10px 30px rgba(0,0,0,.12);overflow:hidden}

  .side-band{position:absolute;left:0;top:70px;width:175px;height:750px;background:var(--lavender)}
  .brand-box{position:absolute;left:18px;top:14px;width:140px;height:120px;background:var(--white);display:flex;flex-direction:column;align-items:center;justify-content:center;gap:8px;text-align:center}
  .brand-dot{width:30px;height:30px;border-radius:50%;background:var(--lavender)}
  .brand-name{font-family:"Cormorant Garamond",Georgia,serif;font-weight:600;font-size:12px;letter-spacing:1.5px;text-transform:uppercase;color:var(--lavender-deep);line-height:1.25;padding:0 8px}
  .brand-rule{position:absolute;left:175px;top:70px;width:355px;height:1px;background:var(--lavender)}

  .tagline{position:absolute;left:87px;top:390px;transform:translate(-50%,-50%) rotate(-90deg);white-space:nowrap;text-align:center;text-transform:uppercase}
  .tagline-top{display:block;font-size:25px;font-weight:500;color:var(--white);letter-spacing:1px}
  .tagline-bottom{display:inline-block;margin-top:4px;padding:2px 8px;background:var(--white);font-size:22px;font-weight:600;color:var(--lavender-deep);letter-spacing:.5px}

  .contact{position:absolute;left:0;top:660px;width:175px;padding:0 14px;color:var(--white)}
  .contact-title{font-size:15px;font-weight:700;padding-bottom:4px;border-bottom:1px solid var(--white);margin-bottom:6px}
  .contact-list{list-style:none;font-size:10px;line-height:1.35}
  .contact-list li{display:flex;gap:5px;align-items:flex-start;margin-bottom:3px}
  .contact-list svg{flex:none;width:10px;height:10px;margin-top:2px}

  .services-pill{position:absolute;right:18px;top:56px;width:170px;height:30px;border-radius:15px;background:var(--lavender);color:var(--white);font-family:"Cormorant SC",Georgia,serif;font-weight:700;font-size:19px;letter-spacing:1px;display:flex;align-items:center;justify-content:center}

  .col-divider{position:absolute;left:352px;top:96px;width:1px;height:710px;background:var(--lavender)}
  .service-col{position:absolute;width:160px;display:flex;flex-direction:column;gap:14px}
  .col-left{left:187px;top:100px}
  .col-right{left:362px;top:130px}
  .service-photo{width:100%;height:112px}
  .service-name{font-family:"Cormorant SC",Georgia,serif;font-weight:700;font-size:13px;margin-top:5px;line-height:1.05}
  .service-text{font-size:9.5px;line-height:1.25;color:var(--muted);margin-top:3px}
  .service{padding-bottom:10px;border-bottom:1px solid var(--lavender)}
  .service:last-child{border-bottom:none}
</style>
</head>
<body>
<main class="flyer">
  <div class="side-band"></div>
  <div class="brand-rule"></div>
  <div class="brand-box">
    <span class="brand-dot"></span>
    <span class="brand-name">Velvet Horizon Aesthetics</span>
  </div>

  <h1 class="tagline">
    <span class="tagline-top">We Change the World</span>
    <span class="tagline-bottom">One Beautiful Face at a Time</span>
  </h1>

  <section class="contact">
    <h2 class="contact-title">Contact Us</h2>
    <ul class="contact-list">
      <li><svg viewBox="0 0 10 10"><circle cx="5" cy="5" r="4" fill="none" stroke="#fff"/><path d="M1 5h8M5 1c2 2 2 6 0 8M5 1c-2 2-2 6 0 8" fill="none" stroke="#fff" stroke-width=".7"/></svg>www.vhaesthetics-demo.com</li>
      <li><svg viewBox="0 0 10 10"><rect x="1" y="2.5" width="8" height="5.5" fill="none" stroke="#fff"/><path d="M1 2.5l4 3 4-3" fill="none" stroke="#fff"/></svg>hello@vhaesthetics-demo.com</li>
      <li><svg viewBox="0 0 10 10"><path d="M2 1l2 .5.5 2-1 1c.6 1.3 1.5 2.2 2.8 2.8l1-1 2 .5.5 2C7 9 1 3 2 1z" fill="#fff"/></svg>(936) 555-0148</li>
      <li><svg viewBox="0 0 10 10"><path d="M5 9.5S1.5 5.8 1.5 3.8a3.5 3.5 0 0 1 7 0C8.5 5.8 5 9.5 5 9.5z" fill="#fff"/><circle cx="5" cy="3.8" r="1.2" fill="#b19cd6"/></svg>1200 Demo Lane<br>Conroe, TX 77301<br>(Next to Conroe Square)</li>
    </ul>
  </section>

  <div class="services-pill">OUR SERVICES</div>
  <div class="col-divider"></div>

  <section class="service-col col-left">
    <article class="service">
      <div class="service-photo" style="background:var(--photo-warm)" role="img" aria-label="Photo of a weight loss injection pen"></div>
      <h3 class="service-name">Weightloss</h3>
      <p class="service-text">Medically guided weight loss plans using proven injections to curb appetite, steady blood sugar and support lasting results.</p>
    </article>
    <article class="service">
      <div class="service-photo" style="background:var(--photo-cool)" role="img" aria-label="Photo of a client receiving a facial treatment"></div>
      <h3 class="service-name">Fibrin Growth Factor (FGF)</h3>
      <p class="service-text">Your own plasma is spun into a fibrin gel that restores volume, smooths lines and boosts natural collagen growth.</p>
    </article>
    <article class="service">
      <div class="service-photo" style="background:var(--photo-peel)" role="img" aria-label="Photo of a chemical peel being applied"></div>
      <h3 class="service-name">Chemical Peels</h3>
      <p class="service-text">Chemical peels improve skin texture, uneven tone, sun damage and acne scarring.</p>
    </article>
  </section>

  <section class="service-col col-right">
    <article class="service">
      <div class="service-photo" style="background:var(--photo-cool)" role="img" aria-label="Photo of a neurotoxin injection treatment"></div>
      <h3 class="service-name">Neurotoxin (Wrinkle Relaxer)</h3>
      <p class="service-text">A quick injection that softens frown lines, crow's feet and forehead creases for a smoother, refreshed look.</p>
    </article>
    <article class="service">
      <div class="service-photo" style="background:var(--photo-skin)" role="img" aria-label="Photo of a dermal filler treatment"></div>
      <h3 class="service-name">Dermal Fillers</h3>
      <p class="service-text">Hyaluronic acid fillers restore lost volume in cheeks, lips and jawline for soft, natural contour.</p>
    </article>
    <article class="service">
      <div class="service-photo" style="background:var(--photo-skin)" role="img" aria-label="Photo of a microneedling treatment"></div>
      <h3 class="service-name">Microneedling Pen</h3>
      <p class="service-text">Fine needles create tiny channels that trigger collagen, refining pores, fine lines, scars and stretch marks.</p>
    </article>
  </section>
</main>
</body>
</html>
```